Business card

I need a business card design for my consulting company in animal welfare for livestock. I like clean, crisp, simple.

One I imagined was double-sided:
side1: just my name and contact information
side2: silhouette of farm animals. Could be 3 (pig, cow, chicken) or all the species (pig, cow, chicken, duck, sheep, rabbit, etc) that continue the length of the card. I have attached an image of a silhouette style.

But, I am open to any concept.

```html
<!DOCTYPE html>
<html lang="en">
<head>
<meta charset="utf-8">
<title>Helen Marwood – Business Card</title>
<link href="https://fonts.googleapis.com/css2?family=Roboto+Condensed:wght@700&family=Open+Sans:wght@400&display=swap" rel="stylesheet">
<style>
  :root {
    --bg: #e9e7e3;
    --card: #ffffff;
    --ink: #55524d;
    --ink-soft: #6f6b65;
    --band-light: #dedbcb;
    --band-dark: #aeab9c;
    --mark: #9c9690;
    --figure-dark: #a3a19e;
    --figure-light: #d2d0cd;
  }
  * { box-sizing: border-box; margin: 0; padding: 0; }
  html, body { width: 1200px; height: 703px; overflow: hidden; background: var(--bg); }
  .canvas { position: relative; width: 1200px; height: 703px; }

  .card {
    position: absolute; top: 208px; width: 500px; height: 286px;
    background: var(--card); overflow: hidden;
    box-shadow: 0 4px 14px rgba(0,0,0,.18);
  }
  .card--front { left: 70px; }
  .card--back { left: 630px; }

  .pattern-band {
    position: absolute; left: 0; right: 0;
    background: linear-gradient(90deg, var(--band-light), var(--band-dark) 50%, var(--band-light));
  }
  .card--front .pattern-band--top { top: 0; height: 30px; }
  .card--front .pattern-band--bottom { bottom: 0; height: 42px; }
  .card--back .pattern-band--top { top: 0; height: 36px; }
  .card--back .pattern-band--bottom { bottom: 0; height: 36px; }

  .identity { position: absolute; left: 28px; top: 54px; display: flex; align-items: center; gap: 14px; }
  .identity__mark { width: 44px; height: 44px; border-radius: 50%; background: var(--mark); flex: none; }
  .identity__name {
    font-family: "Roboto Condensed", sans-serif; font-weight: 700;
    font-size: 17px; letter-spacing: .5px; color: var(--ink); text-transform: uppercase;
  }
  .identity__tagline {
    font-family: "Open Sans", sans-serif; font-size: 9.5px; color: var(--ink-soft); margin-top: 3px;
  }

  .contact {
    position: absolute; right: 28px; top: 132px; list-style: none;
    font-family: "Open Sans", sans-serif; font-size: 10px; color: var(--ink-soft);
  }
  .contact__item { display: flex; align-items: center; gap: 8px; margin-bottom: 5px; }
  .contact__icon { width: 11px; height: 11px; fill: var(--ink); flex: none; }

  .animal-silhouettes {
    position: absolute; left: 160px; top: 72px; width: 180px; height: 126px;
    border-radius: 6px;
    background: linear-gradient(160deg, var(--figure-light), var(--figure-dark));
  }
</style>
</head>
<body>
<main class="canvas">
  <section class="card card--front" aria-label="Card front">
    <div class="pattern-band pattern-band--top" role="img" aria-label="Decorative band of vertical stripes in beige and olive grey"></div>
    <div class="identity">
      <div class="identity__mark"></div>
      <div>
        <h1 class="identity__name">Helen Marwood</h1>
        <p class="identity__tagline">Welfare Services for Livestock Stakeholders</p>
      </div>
    </div>
    <ul class="contact">
      <li class="contact__item">
        <svg class="contact__icon" viewBox="0 0 24 24"><path d="M6.6 10.8a15.1 15.1 0 0 0 6.6 6.6l2.2-2.2a1 1 0 0 1 1-.25 11.4 11.4 0 0 0 3.6.57 1 1 0 0 1 1 1V20a1 1 0 0 1-1 1A17 17 0 0 1 3 4a1 1 0 0 1 1-1h3.5a1 1 0 0 1 1 1c0 1.25.2 2.45.57 3.6a1 1 0 0 1-.25 1z"/></svg>
        <span>+1.555.014.2290</span>
      </li>
      <li class="contact__item">
        <svg class="contact__icon" viewBox="0 0 24 24"><circle cx="12" cy="12" r="10"/><path d="M2 12h20M12 2c3 3 3 17 0 20M12 2c-3 3-3 17 0 20" stroke="#fff" stroke-width="1.5" fill="none"/></svg>
        <span>helen.marwood@mailbox.net</span>
      </li>
    </ul>
    <div class="pattern-band pattern-band--bottom" role="img" aria-label="Decorative band of vertical stripes in beige and olive grey"></div>
  </section>

  <section class="card card--back" aria-label="Card back">
    <div class="pattern-band pattern-band--top" role="img" aria-label="Decorative band of vertical stripes in beige and olive grey"></div>
    <div class="animal-silhouettes" role="img" aria-label="Grey silhouettes of a cow, a pig and a rooster"></div>
    <div class="pattern-band pattern-band--bottom" role="img" aria-label="Decorative band of vertical stripes in beige and olive grey"></div>
  </section>
</main>
</body>
</html>
```